VELora Brand Website

VELora is a multi-retailer concept store of luxury and contemporary timepieces. It has 4 stores all over Indonesia. Targetting young executives who are active and working daily; in their early career and have high aspiration. Keywords: Luxury/Premium, Stylish, Quality, Respect and Loyal.

A few brands carried by VELora boutique: Varnok, Pemra, LUN Favrel, Oskavelde, Fleur et Dantoux, Pike&Vane, Melisse, Vamu, Zenpo, Orvu, Krestwold, Velta, Lanckorn, KIRE.

VELora is an exclusive retail concept of Orvane Holdings (www.orvaneholdings.co.id) and a sister brand of The Quarzo House (www.thequarzohouse.co.id)

The brand color are grey and white. The final design should communicate luxury, modern and fun.

```html
<!DOCTYPE html>
<html lang="en">
<head>
<meta charset="utf-8">
<title>VELora Brand Website</title>
<link rel="stylesheet" href="https://fonts.googleapis.com/css2?family=Kalam:wght@700&family=Open+Sans:wght@400&display=swap">
<style>
  :root {
    --brand-blue: #1f97e4;
    --brand-blue-light: #2aa6ec;
    --sidebar-bg: #272727;
    --sidebar-line: #333333;
    --icon-grey: #8a8a8a;
    --hero-dark: #1b1b1b;
    --hero-mid: #3a3a3a;
    --hero-light: #5a5a5a;
    --text-white: #ffffff;
  }
  * { margin: 0; padding: 0; box-sizing: border-box; }
  html, body {
    width: 1200px;
    height: 703px;
    overflow: hidden;
    background: var(--hero-dark);
  }
  .site {
    position: relative;
    width: 1200px;
    height: 703px;
    overflow: hidden;
    display: flex;
  }
  .sidebar {
    width: 71px;
    height: 100%;
    background: var(--sidebar-bg);
    flex-shrink: 0;
  }
  .menu-toggle {
    height: 72px;
    background: var(--brand-blue-light);
    display: flex;
    align-items: center;
    justify-content: center;
  }
  .nav-item {
    height: 64px;
    border-bottom: 1px solid var(--sidebar-line);
    display: flex;
    align-items: center;
    justify-content: center;
  }
  .nav-item svg { width: 18px; height: 18px; fill: var(--icon-grey); }
  .main {
    flex: 1;
    height: 100%;
    display: flex;
    flex-direction: column;
  }
  .masthead {
    height: 103px;
    background: var(--brand-blue);
    display: flex;
    align-items: center;
    justify-content: center;
  }
  .masthead-title {
    font-family: "Kalam", cursive;
    font-weight: 700;
    font-size: 76px;
    color: var(--text-white);
    line-height: 1;
    margin-top: 10px;
    letter-spacing: 0.5px;
  }
  .hero {
    flex: 1;
    background: radial-gradient(ellipse at 90% 20%, var(--hero-light) 0%, var(--hero-mid) 40%, var(--hero-dark) 85%);
    text-align: center;
    color: var(--text-white);
    font-family: "Open Sans", sans-serif;
  }
  .hero-welcome {
    font-weight: 400;
    font-size: 58px;
    margin-top: 95px;
    line-height: 1.2;
  }
  .hero-tagline {
    font-weight: 400;
    font-size: 42px;
    text-transform: uppercase;
    line-height: 1.25;
    margin-top: 58px;
    letter-spacing: 0.5px;
  }
  .hero-intro {
    font-size: 22px;
    line-height: 33px;
    width: 640px;
    margin: 100px auto 0;
  }
</style>
</head>
<body>
<div class="site">
  <nav class="sidebar" aria-label="Site navigation">
    <div class="menu-toggle">
      <svg width="30" height="24" viewBox="0 0 30 24" aria-hidden="true">
        <rect x="0" y="1" width="30" height="3.5" fill="#ffffff"/>
        <rect x="0" y="10" width="30" height="3.5" fill="#ffffff"/>
        <rect x="0" y="19" width="30" height="3.5" fill="#ffffff"/>
      </svg>
    </div>
    <div class="nav-item"><svg viewBox="0 0 16 16"><path d="M8 1 0 8h2v7h4v-5h4v5h4V8h2z"/></svg></div>
    <div class="nav-item"><svg viewBox="0 0 16 16"><circle cx="8" cy="5" r="3.5"/><path d="M1 15c0-4 3-6 7-6s7 2 7 6z"/></svg></div>
    <div class="nav-item"><svg viewBox="0 0 16 16"><circle cx="5" cy="5" r="2.5"/><circle cx="11" cy="5" r="2.5"/><path d="M0 13c0-3 2-5 5-5s5 2 5 5zM8 13c0-3 1-5 3-5 3 0 5 2 5 5z"/></svg></div>
    <div class="nav-item"><svg viewBox="0 0 16 16"><path d="M0 1h3l1 2h12l-2 7H5l-1 2h10v1.5H2l2-4L2 2.5H0z"/><circle cx="5" cy="14.5" r="1.5"/><circle cx="13" cy="14.5" r="1.5"/></svg></div>
    <div class="nav-item"><svg viewBox="0 0 16 16"><path d="M3 0h7l4 4v12H3zM10 0v4h4z"/></svg></div>
    <div class="nav-item"><svg viewBox="0 0 16 16"><path d="M2 3h12v8H2zm1 1v6h10V4zM0 12h16v2H0z"/></svg></div>
    <div class="nav-item"><svg viewBox="0 0 16 16"><path d="M8 1 0 8h2v7h4v-5h4v5h4V8h2z"/></svg></div>
    <div class="nav-item"><svg viewBox="0 0 16 16"><circle cx="5" cy="5" r="2.5"/><circle cx="11" cy="5" r="2.5"/><path d="M0 13c0-3 2-5 5-5s5 2 5 5zM8 13c0-3 1-5 3-5 3 0 5 2 5 5z"/></svg></div>
    <div class="nav-item"><svg viewBox="0 0 16 16"><path d="M0 3h6l1.5 2H16v9H0z"/></svg></div>
  </nav>
  <main class="main">
    <header class="masthead">
      <h1 class="masthead-title">VELora Brand Website</h1>
    </header>
    <section class="hero">
      <h2 class="hero-welcome">Welcome</h2>
      <p class="hero-tagline">We provide best collection of watches<br>to choose from</p>
      <p class="hero-intro">VELora is a multi-retailer concept store of luxury and contemporary timepieces. It has 4 stores all over Indonesia. Targetting young executives who are active and working daily; in their early career and have high aspiration.</p>
    </section>
  </main>
</div>
</body>
</html>
```